Webdesign für Immobilienmanagement
Zielgruppe
Immobilienmanagement Unternehmen / allg. Hausverwaltung , Hausmeisterservice, Grünanlagenpflege, Unterhaltsreinigung, Winterdienst
Zielgruppe: Mieter und Wohnungseigentümer
Aufgabenstellung
Farben: weiß/grün
keine Kopie der alten Seite
nutzerfreundliche Unternehmenswebseite
Logo vorhanden auf alter Webseite

```html
<!DOCTYPE html>
<html lang="de">
<head>
<meta charset="utf-8">
<title>LIWA Immobilien-Management</title>
<link href="https://fonts.googleapis.com/css2?family=Titillium+Web:wght@300;400;600;700&display=swap" rel="stylesheet">
<style>
:root{
  --green:#4caf33;
  --green-soft:#7fc66b;
  --green-pale:#d4ebcc;
  --navy:#0f2f5f;
  --ink:#1d1d1d;
  --text:#555;
  --grey:#f4f4f4;
  --band:#e6e6e6;
  --field:#e4e4e4;
}
*{box-sizing:border-box;margin:0;padding:0}
html,body{width:1200px;height:2439px;overflow:hidden;background:#fff}
body{position:relative;font-family:"Titillium Web",sans-serif;color:var(--text)}
.abs{position:absolute}
a{color:inherit;text-decoration:none}

.topbar{left:0;top:0;width:1200px;height:40px;border-bottom:1px solid #e3e3e3;font-size:8.5px;color:#444}
.topbar .member{left:125px;top:11px;display:flex;align-items:center;gap:10px}
.topbar .contact{right:125px;top:13px;display:flex;gap:22px}
.topbar .contact span{display:flex;align-items:center;gap:6px}
.dot{width:18px;height:18px;border:1.5px solid #8aa3c4;border-radius:50%}

.brand{left:125px;top:66px;display:flex;align-items:center;gap:8px;font-weight:700;font-size:22px;color:var(--green);letter-spacing:1px}
.brand .sq{width:22px;height:22px;background:var(--green)}
.nav-divider{left:282px;top:62px;width:1px;height:38px;background:#ddd}
.nav{left:322px;top:72px;display:flex;gap:20px;font-size:11px;font-weight:600;color:#999;letter-spacing:.3px}
.nav .active{color:var(--green)}
.emergency{left:921px;top:70px;width:154px;font-size:11px;font-weight:700;color:var(--green);border-bottom:3px solid var(--green);padding-bottom:4px;display:flex;justify-content:space-between;align-items:center}

.hero-band{left:0;top:205px;width:1200px;height:337px;background:var(--band)}
.hero-panel{left:483px;top:140px;width:592px;height:466px;background:var(--green-soft);border-radius:8px}
.hero-panel::after{content:"";position:absolute;left:0;right:0;top:65px;height:337px;background:rgba(0,0,0,.05)}
.hero-photo{left:125px;top:173px;width:475px;height:400px;border-radius:8px;background:linear-gradient(135deg,#e9e5df,#cdbfa9 60%,#b89a72)}
.hero-copy{left:647px;top:300px;width:420px;color:#fff}
.eyebrow{display:flex;align-items:center;gap:14px;font-size:15px;font-weight:300}
.eyebrow::before{content:"";width:25px;height:3px;background:var(--navy)}
.hero-copy h1{font-size:29px;font-weight:700;line-height:40px;margin-top:6px}
.link{display:inline-flex;align-items:center;gap:10px;font-size:11px;font-weight:700;color:var(--navy);border-bottom:3px solid var(--navy);padding-bottom:3px}
.hero-copy .link{margin-top:16px}
.arrow-btn{top:353px;width:40px;height:40px;background:var(--navy);display:flex;align-items:center;justify-content:center}

.service{top:674px;width:140px;height:140px;background:var(--grey);border-radius:0 0 16px 16px;text-align:center;padding-top:30px;font-size:11px;font-weight:700;color:var(--navy);line-height:15px}
.service svg{display:block;margin:0 auto 8px}
.more-services{left:957px;top:842px}

.about-band{left:0;top:943px;width:1200px;height:494px;background:var(--grey)}
.about-copy{left:125px;top:1024px;width:460px}
.about-copy .label{display:flex;align-items:center;gap:14px;font-size:11px;color:var(--green)}
.about-copy .label::before{content:"";width:25px;height:3px;background:var(--navy)}
.about-copy h2{font-size:28px;font-weight:700;color:var(--navy);line-height:40px;margin-top:8px}
.about-copy h2 em{font-style:normal;color:var(--green)}
.about-copy p{font-size:11px;line-height:20px;margin-top:12px}
.checks{list-style:none;margin-top:20px;font-size:11px}
.checks li{display:flex;align-items:center;gap:12px;height:27px}
.about-copy .link{margin-top:18px}
.about-accent{left:622px;top:1059px;width:80px;height:262px;background:var(--green-pale);border-radius:8px}
.about-photo{left:662px;top:1024px;width:413px;height:333px;border-radius:8px;background:linear-gradient(180deg,#f2ef9a,#a9cf4a 45%,#4f8f22)}

.callback-band{left:20px;top:1548px;width:1159px;height:261px;background:#f7f7f7;border-radius:8px}
.callback-photo{left:600px;top:1548px;width:579px;height:261px;border-radius:0 8px 8px 0;background:linear-gradient(90deg,#d8d2c9,#ececea 55%,#e2e2e0)}
.form-card{left:125px;top:1518px;width:475px;height:322px;background:#fff;border-radius:8px;box-shadow:0 2px 8px rgba(0,0,0,.12);padding:40px 40px 0}
.form-card .kicker{font-size:10.5px;font-weight:600;color:var(--navy)}
.form-card h3{font-size:20px;font-weight:600;color:var(--ink);margin:4px 0 6px}
.grid{display:grid;grid-template-columns:1fr 1fr;gap:10px}
.field{height:30px;background:var(--field);font-size:7px;color:#777;padding:10px 5px;display:flex;justify-content:space-between}
.field.area{height:58px;grid-column:1/3}
.submit{margin-top:10px;height:37px;background:var(--green);color:#fff;font-size:11px;font-weight:700;display:flex;align-items:center;justify-content:center}

.kontakt{left:125px;top:1962px;font-size:38px;font-weight:700;color:var(--ink);letter-spacing:.5px}
.f-col{top:2042px;font-size:11px;color:#333;line-height:17px}
.f-col strong{color:var(--ink);font-weight:700}
.f-col .g{color:var(--green);font-weight:600}
.f-col .row{display:flex;align-items:center;gap:8px}
.f-nav{list-style:none;font-weight:700;color:var(--ink)}
.f-nav li{height:30px}
.footer-brand{left:925px;top:2052px;display:flex;align-items:center;gap:8px;font-weight:700;font-size:20px;color:var(--green);letter-spacing:1px}
.footer-brand .sq{width:22px;height:22px;background:var(--green)}
.f-rule{left:125px;top:2296px;width:231px;height:2px;background:var(--green)}
.copy{left:125px;top:2309px;font-size:8px;color:#555}
.legal{left:125px;top:2330px;font-size:8px;color:#444;display:flex;gap:10px}
.legal a{text-decoration:underline}
</style>
</head>
<body>

<header class="abs topbar">
  <div class="abs member"><span class="dot"></span>Mitglied im Netzwerk Wohnen &amp; Verwalten Elbtal e.V</div>
  <div class="abs contact">
    <span><svg width="12" height="9" viewBox="0 0 12 9"><rect x=".5" y=".5" width="11" height="8" fill="none" stroke="#999"/><path d="M.5 .5l5.5 4.5 5.5-4.5" fill="none" stroke="#999"/></svg>info@liwa-immobilien.example</span>
    <span><svg width="7" height="11" viewBox="0 0 7 11"><rect x=".5" y=".5" width="6" height="10" rx="1" fill="none" stroke="#999"/></svg>+49 30 1234 567-0</span>
  </div>
</header>

<div class="abs brand"><span>LIWA</span><span class="sq"></span></div>
<div class="abs nav-divider"></div>
<nav class="abs nav">
  <a class="active">STARTSEITE</a><a>ÜBER UNS</a><a>HAUSVERWALTUNG</a><a>HAUSMEISTER</a><a>DOWNLOADS</a><a>KONTAKT</a><a>PARTNER</a>
</nav>
<a class="abs emergency">24 STUNDEN NOTDIENST <svg width="20" height="10" viewBox="0 0 20 10"><path d="M0 5h17M12 1l5 4-5 4" fill="none" stroke="currentColor" stroke-width="2.5"/></svg></a>

<section>
  <div class="abs hero-band"></div>
  <div class="abs hero-panel"></div>
  <div class="abs hero-photo" role="img" aria-label="Foto: Paar mit Hausmodell und Schlüssel in einer Wohnung voller Umzugskartons"></div>
  <div class="abs hero-copy">
    <div class="eyebrow">Regional &amp; überregional seit fast 30 Jahren</div>
    <h1>Ihr zuverlässiger Dienstleister rund um die Immobilie</h1>
    <a class="link">UNSERE LEISTUNGEN <svg width="20" height="10" viewBox="0 0 20 10"><path d="M0 5h17M12 1l5 4-5 4" fill="none" stroke="currentColor" stroke-width="2.5"/></svg></a>
  </div>
  <div class="abs arrow-btn" style="left:20px"><svg width="22" height="12" viewBox="0 0 22 12"><path d="M22 6H4M9 1L3 6l6 5" fill="none" stroke="#fff" stroke-width="3"/></svg></div>
  <div class="abs arrow-btn" style="left:1140px"><svg width="22" height="12" viewBox="0 0 22 12"><path d="M0 6h18M13 1l6 5-6 5" fill="none" stroke="#fff" stroke-width="3"/></svg></div>
</section>

<section>
  <div class="abs service" style="left:20px"><svg width="40" height="40" viewBox="0 0 40 40"><path d="M5 19L20 6l15 13" fill="none" stroke="#4caf33" stroke-width="2.5"/><path d="M9 16v19h22V16" fill="none" stroke="#4caf33" stroke-width="2.5"/><rect x="17" y="24" width="6" height="11" fill="#0f2f5f"/></svg>ALLGEMEINE<br>HAUSVERWALTUNG</div>
  <div class="abs service" style="left:190px"><svg width="40" height="40" viewBox="0 0 40 40"><circle cx="20" cy="20" r="14" fill="none" stroke="#4caf33" stroke-width="2.5"/><path d="M25 14c-4-3-10-1-10 6s6 9 10 6M12 18h9M12 22h9" fill="none" stroke="#0f2f5f" stroke-width="2.5"/></svg>KAUFMÄNNISCHE<br>BETREUUNG</div>
  <div class="abs service" style="left:360px"><svg width="40" height="40" viewBox="0 0 40 40"><circle cx="20" cy="20" r="8" fill="none" stroke="#0f2f5f" stroke-width="2.5"/><path d="M20 4v6M20 30v6M4 20h6M30 20h6M9 9l4 4M27 27l4 4M31 9l-4 4M9 31l4-4" stroke="#4caf33" stroke-width="2.5"/></svg>TECHNISCHE<br>BETREUUNG</div>
  <div class="abs service" style="left:530px"><svg width="40" height="40" viewBox="0 0 40 40"><path d="M8 32l14-14" stroke="#0f2f5f" stroke-width="4" stroke-linecap="round"/><path d="M22 18a8 8 0 1 0 6-12l-4 5 3 4 5-3a8 8 0 0 1-10 6" fill="none" stroke="#4caf33" stroke-width="2.5"/></svg>HAUSMEISTER<br>SERVICE</div>
  <div class="abs service" style="left:700px"><svg width="40" height="40" viewBox="0 0 40 40"><path d="M8 32C8 16 18 8 33 7c0 15-8 25-25 25z" fill="none" stroke="#4caf33" stroke-width="2.5"/><path d="M8 32L24 16" stroke="#0f2f5f" stroke-width="2.5"/></svg>GRÜNANLAGEN<br>PFLEGE</div>
  <div class="abs service" style="left:869px"><svg width="40" height="40" viewBox="0 0 40 40"><path d="M20 5c6 9 11 14 11 20a11 11 0 0 1-22 0c0-6 5-11 11-20z" fill="none" stroke="#4caf33" stroke-width="2.5"/><path d="M15 26a5 5 0 0 0 5 5" fill="none" stroke="#0f2f5f" stroke-width="2.5"/></svg>UNTERHALTS<br>REINIGUNG</div>
  <div class="abs service" style="left:1040px"><svg width="40" height="40" viewBox="0 0 40 40"><path d="M20 4v32M6 12l28 16M6 28l28-16" stroke="#4caf33" stroke-width="2.5"/><path d="M16 6l4 4 4-4M16 34l4-4 4 4" fill="none" stroke="#0f2f5f" stroke-width="2.5"/></svg>WINTERDIENST</div>
  <a class="abs link more-services">MEHR ERFAHREN <svg width="20" height="10" viewBox="0 0 20 10"><path d="M0 5h17M12 1l5 4-5 4" fill="none" stroke="currentColor" stroke-width="2.5"/></svg></a>
</section>

<section>
  <div class="abs about-band"></div>
  <div class="abs about-copy">
    <div class="label">LIWA Immobilien-Management GmbH!</div>
    <h2>Wohnen und arbeiten im <em>Grünen.</em><br>Dafür steht <em>LIWA.</em></h2>
    <p>Wir sind ein junges, freundliches, gut ausgebildetes Team, das sich mit all seiner Aufmerksamkeit und Kompetenz um Ihre Wünsche in Sachen Immobilien kümmert. Möchten Sie eine Wohnung mieten, suchen Sie einen Hausmeister, oder einen Verwalter für Ihre Immobilie?</p>
    <ul class="checks">
      <li><svg width="14" height="11" viewBox="0 0 14 11"><path d="M1 5.5l4 4L13 1" fill="none" stroke="#4caf33" stroke-width="2.5"/></svg>zuverlässige Verwaltung</li>
      <li><svg width="14" height="11" viewBox="0 0 14 11"><path d="M1 5.5l4 4L13 1" fill="none" stroke="#4caf33" stroke-width="2.5"/></svg>günstige Konditionen</li>
      <li><svg width="14" height="11" viewBox="0 0 14 11"><path d="M1 5.5l4 4L13 1" fill="none" stroke="#4caf33" stroke-width="2.5"/></svg>Erhalt und Verbesserung der Mietsache</li>
      <li><svg width="14" height="11" viewBox="0 0 14 11"><path d="M1 5.5l4 4L13 1" fill="none" stroke="#4caf33" stroke-width="2.5"/></svg>partnerschaftiche Beziehung zu den Mietern</li>
    </ul>
    <a class="link">MEHR ERFAHREN <svg width="20" height="10" viewBox="0 0 20 10"><path d="M0 5h17M12 1l5 4-5 4" fill="none" stroke="currentColor" stroke-width="2.5"/></svg></a>
  </div>
  <div class="abs about-accent"></div>
  <div class="abs about-photo" role="img" aria-label="Foto: kleines Hausmodell im grünen Gras mit Gänseblümchen"></div>
</section>

<section>
  <div class="abs callback-band"></div>
  <div class="abs callback-photo" role="img" aria-label="Foto: lächelnde Mitarbeiterin mit Brille am Telefon"></div>
  <form class="abs form-card">
    <div class="kicker">Sie haben eine Frage zu unserem Serviceangebot?</div>
    <h3>Wir rufen Sie gerne zurück!</h3>
    <div class="grid">
      <div class="field">Name</div>
      <div class="field">Telefon</div>
      <div class="field">E-Mail</div>
      <div class="field">Bereich <svg width="8" height="5" viewBox="0 0 8 5"><path d="M.5.5L4 4 7.5.5" fill="none" stroke="#555"/></svg></div>
      <div class="field area">Nachricht</div>
    </div>
    <div class="submit">JETZT NACHRICHT SENDEN</div>
  </form>
</section>

<footer>
  <h2 class="abs kontakt">KONTAKT</h2>
  <div class="abs f-col" style="left:125px">
    <strong>LIWA Immobilien-Management GmbH</strong><br>Lindenweg 8 B<br>D-04100 Musterstadt
    <div class="row" style="margin-top:12px"><svg width="11" height="11" viewBox="0 0 11 11"><path d="M2 0l2 3-1 1.5c.8 1.6 2 2.8 3.5 3.5L8 7l3 2-1.5 2C5 10.5.5 6 0 1.5z" fill="#4caf33"/></svg>+49 30 1234 567-0</div>
    <div class="row"><svg width="11" height="8" viewBox="0 0 11 8"><rect width="11" height="8" fill="#4caf33"/><path d="M0 0l5.5 4.5L11 0" fill="none" stroke="#fff"/></svg>info@liwa-immobilien.example</div>
    <div style="margin-top:24px"><strong>Social Media</strong></div>
    <div class="row" style="margin-top:6px;gap:10px"><span style="width:15px;height:15px;border:2px solid #4caf33;border-radius:50%"></span><span style="width:15px;height:15px;background:#4caf33"></span><span style="width:15px;height:15px;background:#4caf33"></span></div>
  </div>
  <ul class="abs f-col f-nav" style="left:447px">
    <li>Über Uns</li><li>Hausverwaltung</li><li>Hausmeister</li><li>Downloads</li><li>Kontakt</li><li>Partner</li><li>Karriere</li><li class="g">24-Stunden Notdienst</li>
  </ul>
  <div class="abs f-col" style="left:641px;width:240px">
    <strong>Unsere Geschäftszeiten</strong><br><br>
    Montag <span class="g">09.00 - 12.00 Uhr</span><br>
    Dienstag <span class="g">09.00 - 12.00 &amp; 13.00 - 15.00 Uhr</span><br>
    Donnerstag <span class="g">09.00 - 12.00 &amp; 13.00 - 18.00 Uhr</span><br><br>
    Gesprächstermine außerhalb unserer Geschäftszeiten sind jederzeit nach vorheriger Vereinbarung möglich.
  </div>
  <div class="abs footer-brand"><span>LIWA</span><span class="sq"></span></div>
  <div class="abs f-rule"></div>
  <div class="abs copy">© 2024 LIWA Immobilien-Management GmbH</div>
  <div class="abs legal"><a>AGB</a><a>Datenschutzerklärung</a><a>Impressum</a></div>
</footer>

</body>
</html>
```